Vantrel LLC banner ad design project

I want banner advertisements designed in various ad formats-the most popular sizes according to Brindle Adspace (600x450, 300x250, 250x250, 120x600).
Please put in the ads a picture of the bottle (attached) and a picture of a slim woman/man (preferably woman, as I am targetting a largely female audience) in the advertisement.
As for the text of the ads, I'd like for there to be something like the following:
"Lose 15 lbs in 3 months"
"Lose weight with traditional Chinese medicine"
"Lose weight using ancient Chinese herbs"
Also please feel free to use other text using some of the articles on my site, which can be found at the following link:
http://www.vantrel-shop.com/
Thanks, and if you have any additional questions, please don't hesitate to ask.
Additional notes: would also like for you to follow the color scheme on my website (orange, green) for the most part, although please when submitting different ads make sure to include other color schemes, as some of those color schemes may work better for the ads than the green/orange color scheme.
I've also attached an ad from Plenafirm that should give you an idea of something similar I'm looking for (though please submit multiple ideas)!

```html
<!DOCTYPE html>
<html lang="en">
<head>
<meta charset="utf-8">
<title>Vantrel banner set</title>
<link href="https://fonts.googleapis.com/css2?family=Cabin:wght@400;500;600;700&display=swap" rel="stylesheet">
<style>
  :root {
    --stage: #717171;
    --green: #1f9a3e;
    --green-dark: #17873a;
    --orange: #e8682a;
    --orange-deep: #d9531b;
    --text-gray: #6b6b6b;
    --panel-light: #f1f1f1;
    --teal: #2bb08e;
    --teal-light: #6fd6b8;
    --sun: #f7c843;
    --badge-blue: #1aa0d6;
    --white: #ffffff;
  }
  * { box-sizing: border-box; margin: 0; padding: 0; }
  html, body { width: 1200px; height: 750px; overflow: hidden; }
  body { background: var(--stage); font-family: "Cabin", Arial, sans-serif; position: relative; }

  .banner { position: absolute; overflow: hidden; background: var(--white); }
  .abs { position: absolute; }
  .photo { position: absolute; }
  .brand { position: absolute; color: var(--orange); font-weight: 600; letter-spacing: 0.5px; line-height: 1; }
  .brand-dot { position: absolute; border-radius: 50%; background: var(--orange); }
  .badge {
    position: absolute; border-radius: 50%; background: var(--green); color: var(--white);
    border: 2px solid var(--white); text-align: center; font-style: italic; font-weight: 700; line-height: 1;
    display: flex; flex-direction: column; justify-content: center; align-items: center;
  }
  .cta {
    position: absolute; color: var(--white); font-weight: 500; text-align: center;
    background: linear-gradient(#f3823e, var(--orange-deep));
    display: flex; align-items: center; justify-content: center;
    box-shadow: 0 2px 3px rgba(0,0,0,0.25);
  }

  /* Large 600x450 */
  .banner-large { left: 50px; top: 121px; width: 600px; height: 448px;
    background: linear-gradient(#fafafa, #e9e9e9); }
  .banner-large .scenery { left: 250px; top: 190px; width: 340px; height: 180px;
    background: linear-gradient(rgba(200,200,200,0), rgba(190,190,190,0.45)); }
  .banner-large .headline { left: 283px; top: 43px; width: 292px; text-align: center;
    color: var(--green); font-size: 44px; font-weight: 500; letter-spacing: 1px;
    border-top: 1px solid #9a9a9a; border-bottom: 1px solid #9a9a9a; line-height: 50px; }
  .banner-large .subhead { left: 283px; top: 102px; width: 292px; text-align: center;
    color: var(--orange); font-size: 24px; font-weight: 600; letter-spacing: 3px; }
  .banner-large .tagline { left: 288px; top: 138px; width: 300px; text-align: center;
    color: var(--text-gray); font-size: 18px; }
  .banner-large .benefits { left: 302px; top: 178px; list-style: none; color: var(--text-gray); font-size: 16px; }
  .banner-large .benefits li { height: 26px; }
  .banner-large .benefits li::before { content: "•"; margin-right: 8px; font-size: 13px; }
  .banner-large .benefits em { font-style: normal; color: var(--green); }
  .banner-large .cta { left: 297px; top: 273px; width: 216px; height: 46px; border-radius: 23px; font-size: 16px; }

  /* Square 250x250 */
  .banner-square { left: 694px; top: 82px; width: 250px; height: 250px;
    background: linear-gradient(#f7f7f7, #e6e6e6); }
  .banner-square .headline { left: 14px; top: 10px; color: var(--orange); font-size: 24px; font-weight: 500; }
  .banner-square .tagline { left: 16px; top: 43px; color: var(--text-gray); font-size: 15px; line-height: 20px; }
  .banner-square .cta { left: 10px; top: 98px; width: 146px; height: 42px; border-radius: 21px; font-size: 14px; }

  /* Rectangle 300x250 */
  .banner-rect { left: 694px; top: 356px; width: 300px; height: 250px;
    background: linear-gradient(135deg, var(--teal), var(--teal-light)); }
  .banner-rect .headline { left: 14px; top: 12px; color: var(--white); font-size: 23px; font-weight: 500; }
  .banner-rect .tagline { left: 16px; top: 45px; color: var(--white); font-size: 16px; line-height: 22px; font-weight: 500; }
  .banner-rect .cta { left: 13px; top: 117px; width: 140px; height: 35px; border-radius: 3px; font-size: 14px; }

  /* Skyscraper 120x600 */
  .banner-sky { left: 1037px; top: 56px; width: 120px; height: 600px;
    background: linear-gradient(#e4591c 20%, #f08a2a 55%, var(--sun)); }
  .banner-sky .headline { left: 0; top: 126px; width: 120px; text-align: center; color: var(--white);
    font-size: 31px; font-weight: 500; line-height: 34px; }
  .banner-sky .subhead { left: 0; top: 198px; width: 120px; text-align: center; color: #ffe08a;
    font-size: 19px; font-weight: 600; line-height: 24px; }
  .banner-sky .cta { left: 7px; top: 270px; width: 109px; height: 77px; border-radius: 3px; font-size: 16px;
    background: linear-gradient(#3ec7a0, #22a07f); border: 2px solid #9fe6cf; line-height: 22px; }
</style>
</head>
<body>

<section class="banner banner-large">
  <div class="abs scenery" role="img" aria-label="Faint traditional Chinese temple scenery"></div>
  <svg class="abs" style="left:0;top:0" width="600" height="448" viewBox="0 0 600 448">
    <path d="M0 435 C200 410 420 360 600 330 L600 448 L0 448 Z" fill="var(--green)"/>
    <path d="M0 441 C210 418 420 372 600 344 L600 448 L0 448 Z" fill="var(--white)"/>
  </svg>
  <div class="photo" style="left:10px;top:58px;width:178px;height:385px;border-radius:18px;background:linear-gradient(90deg,#dcdcdc,#ffffff 50%,#e2e2e2);" role="img" aria-label="Vantrel supplement bottle with herbal label"></div>
  <div class="photo" style="left:178px;top:0;width:92px;height:446px;background:linear-gradient(#f3d2bd,#ee7a3a 35%,#f0c3a4 60%,#eed0bb);border-radius:46px 46px 16px 16px;" role="img" aria-label="Slim woman in orange activewear stretching arms overhead"></div>
  <div class="abs headline">LOSE 15 LBS</div>
  <div class="abs subhead">IN 3 MONTHS</div>
  <div class="abs tagline">with Traditional Chinese Medicine</div>
  <ul class="abs benefits">
    <li>Clinically proven weight loss tool</li>
    <li><em>TARGETS</em> excess belly fat</li>
    <li><em>INCREASES</em> metabolism</li>
  </ul>
  <div class="cta">TRY VANTREL TODAY</div>
  <div class="brand-dot" style="left:488px;top:346px;width:26px;height:26px;"></div>
  <div class="brand" style="left:433px;top:392px;font-size:32px;">VANTREL</div>
  <div class="badge" style="left:140px;top:330px;width:90px;height:90px;font-size:24px;">100%<span style="font-size:16px;font-weight:500">natural</span></div>
</section>

<section class="banner banner-square">
  <div class="photo" style="left:126px;top:26px;width:60px;height:174px;background:linear-gradient(#f1d0bb,#2fa54a 45%,#f0cdb6);border-radius:30px 30px 8px 8px;" role="img" aria-label="Slim woman in green activewear"></div>
  <div class="photo" style="left:172px;top:14px;width:80px;height:166px;border-radius:10px;background:linear-gradient(90deg,#dedede,#ffffff 50%,#e4e4e4);" role="img" aria-label="Vantrel supplement bottle"></div>
  <svg class="abs" style="left:0;top:0" width="250" height="250" viewBox="0 0 250 250">
    <path d="M0 178 C90 190 170 200 250 196 L250 250 L0 250 Z" fill="var(--orange)"/>
    <path d="M0 184 C90 198 170 206 250 204 L250 250 L0 250 Z" fill="var(--white)"/>
  </svg>
  <div class="abs headline">Lose weight</div>
  <div class="abs tagline">using ancient<br>Chinese herbs</div>
  <div class="cta">Try vantrel today</div>
  <div class="brand-dot" style="left:55px;top:166px;width:22px;height:22px;"></div>
  <div class="brand" style="left:9px;top:204px;font-size:25px;">VANTREL</div>
  <div class="badge" style="left:188px;top:172px;width:60px;height:60px;font-size:17px;">100%<span style="font-size:12px;font-weight:500">natural</span></div>
</section>

<section class="banner banner-rect">
  <div class="photo" style="left:146px;top:0;width:66px;height:186px;background:linear-gradient(#f0cdb6,#f6d9c3 40%,#f3e6c8 65%,#ecd0b8);border-radius:8px;" role="img" aria-label="Slim woman's waist and hips"></div>
  <div class="photo" style="left:196px;top:20px;width:104px;height:210px;border-radius:12px;background:linear-gradient(90deg,#dcdcdc,#ffffff 50%,#e2e2e2);" role="img" aria-label="Vantrel supplement bottle"></div>
  <svg class="abs" style="left:0;top:0" width="300" height="250" viewBox="0 0 300 250">
    <path d="M0 166 C100 176 200 200 300 214 L300 250 L0 250 Z" fill="var(--orange)"/>
    <path d="M0 173 C100 184 200 208 300 222 L300 250 L0 250 Z" fill="var(--white)"/>
  </svg>
  <div class="abs headline">Lose weight</div>
  <div class="abs tagline">with traditional<br>Chinese<br>medicine</div>
  <div class="cta">Try vantrel today</div>
  <div class="brand-dot" style="left:57px;top:173px;width:22px;height:22px;"></div>
  <div class="brand" style="left:9px;top:210px;font-size:25px;">VANTREL</div>
  <div class="badge" style="left:160px;top:176px;width:62px;height:62px;font-size:17px;">100%<span style="font-size:12px;font-weight:500">natural</span></div>
</section>

<section class="banner banner-sky">
  <svg class="abs" style="left:0;top:0" width="120" height="120" viewBox="0 0 120 120">
    <path d="M0 0 H120 V72 C80 80 40 92 0 104 Z" fill="var(--teal)"/>
    <path d="M0 0 H120 V66 C80 74 40 86 0 96 Z" fill="var(--white)"/>
  </svg>
  <div class="brand-dot" style="left:48px;top:12px;width:22px;height:22px;"></div>
  <div class="brand" style="left:5px;top:46px;font-size:23px;">VANTREL</div>
  <div class="abs headline">LOSE<br>15 LBS</div>
  <div class="abs subhead">IN 3<br>MONTHS</div>
  <div class="cta">Try<br>Vantrel<br>Today</div>
  <div class="photo" style="left:0;top:358px;width:100px;height:242px;border-radius:10px;background:linear-gradient(90deg,#dcdcdc,#ffffff 50%,#e2e2e2);" role="img" aria-label="Vantrel supplement bottle"></div>
  <div class="photo" style="left:58px;top:414px;width:62px;height:186px;background:linear-gradient(#5a3a2c,#e6b596 30%,#d63a34 65%,#d63a34);border-radius:30px 30px 0 0;" role="img" aria-label="Smiling slim woman in red sports top"></div>
  <div class="badge" style="left:6px;top:533px;width:64px;height:64px;font-size:17px;background:var(--badge-blue);">100%<span style="font-size:12px;font-weight:500">natural</span></div>
</section>

</body>
</html>
```